Trulock Property Inspections

Property Inspection ( pre-purchase building inspections, swimming pool inspection, pest inspection , maintenance)

Industry/Entity Type

Building

Contact Information for Business Card

Omar Tanvelli
info@trulockinspections.com.au
0417 828 691

TruLock Property Inspections
www.trulockinspections.com.au

on the back

Property Inspections
Property Maintenance

Safe Home....Safe Familu

```html
<!DOCTYPE html>
<html lang="en">
<head>
<meta charset="utf-8">
<title>TruLock Property Inspections – Business Card</title>
<link rel="stylesheet" href="https://fonts.googleapis.com/css2?family=Exo+2:wght@600;700&family=Tenor+Sans&display=swap">
<style>
  :root {
    --bg: #d9d9d7;
    --card-white: #f4f4f2;
    --brand-blue: #1f4590;
    --brand-red: #c92027;
    --edge-blue: #b9cbe6;
    --divider: #8f9296;
    --stripe-red: #b8353d;
    --stripe-white: #c9ccd6;
    --text-white: #ffffff;
  }
  * { margin: 0; padding: 0; box-sizing: border-box; }
  html, body { width: 1200px; height: 934px; overflow: hidden; background: var(--bg); }
  .canvas {
    width: 1200px; height: 934px;
    display: flex; flex-direction: column; align-items: center; justify-content: center; gap: 56px;
  }
  .card {
    position: relative; width: 620px; height: 378px;
    background: var(--card-white); overflow: hidden;
    box-shadow: 0 4px 14px rgba(0,0,0,.18);
  }
  .card svg.art { position: absolute; inset: 0; width: 100%; height: 100%; }

  /* back side */
  .logo-panel {
    position: absolute; left: 404px; top: 112px; width: 216px; height: 266px;
    display: flex; flex-direction: column; align-items: center; justify-content: center; gap: 8px;
    color: var(--brand-blue); text-align: center;
  }
  .logo-name { display: flex; align-items: center; gap: 8px;
    font-family: "Exo 2", sans-serif; font-weight: 700; font-size: 19px; line-height: 1.15; }
  .logo-mark { width: 14px; height: 14px; background: var(--brand-blue); flex: none; }
  .logo-tagline, .logo-web { font-family: "Exo 2", sans-serif; font-weight: 600; font-size: 12px; }

  /* front side */
  .identity {
    position: absolute; left: 0; top: 42px; width: 460px; text-align: center;
    color: var(--brand-blue); font-family: "Exo 2", sans-serif;
  }
  .identity .person { font-weight: 700; font-size: 24px; margin-bottom: 4px; }
  .identity .services, .identity .slogan { font-weight: 600; font-size: 15px; line-height: 1.25; }
  .contact {
    position: absolute; left: 330px; top: 226px;
    color: var(--text-white); font-family: "Tenor Sans", sans-serif; font-size: 18px; line-height: 1.22;
  }
  .contact li { list-style: none; display: flex; align-items: center; gap: 8px; }
  .contact li.plain { padding-left: 22px; }
  .contact li.email { font-size: 15px; margin-top: 3px; }
  .contact svg { width: 14px; height: 14px; flex: none; }
</style>
</head>
<body>
<main class="canvas">

  <section class="card card-back" aria-label="Card back">
    <svg class="art" viewBox="0 0 620 378" aria-hidden="true">
      <rect width="620" height="378" fill="var(--divider)"/>
      <rect x="0" y="0" width="400" height="104" fill="var(--brand-red)"/>
      <rect x="404" y="0" width="216" height="108" fill="var(--brand-blue)"/>
      <rect x="0" y="108" width="400" height="270" fill="var(--brand-blue)"/>
      <rect x="404" y="112" width="216" height="266" fill="var(--card-white)"/>
    </svg>
    <div class="logo-panel">
      <div class="logo-name"><span class="logo-mark"></span><span>TruLock Property<br>Inspections</span></div>
      <p class="logo-tagline">Sure Home...Calm Family</p>
      <p class="logo-web">www.trulockinspections.com.au</p>
    </div>
  </section>

  <section class="card card-front" aria-label="Card front">
    <svg class="art" viewBox="0 0 620 378" aria-hidden="true">
      <rect x="0" y="312" width="620" height="46" fill="var(--brand-red)"/>
      <path d="M0,196 H288 Q300,196 304,206 Q308,216 320,216 H620 V344 H328 Q310,344 310,326 V312 H0 Z"
            fill="var(--brand-blue)" stroke="var(--edge-blue)" stroke-width="5"/>
      <g class="stripes">
        <polygon points="72,296 98,222 120,222 94,296" fill="var(--stripe-red)"/>
        <polygon points="118,296 144,222 166,222 140,296" fill="var(--stripe-white)"/>
        <polygon points="164,296 190,222 212,222 186,296" fill="var(--stripe-red)"/>
        <polygon points="210,296 236,222 258,222 232,296" fill="var(--stripe-white)"/>
      </g>
    </svg>
    <div class="identity">
      <h1 class="person">Omar Tanvelli</h1>
      <p class="services">Property Inspections Property Maintenance</p>
      <p class="slogan">Sure Home....Calm Family</p>
    </div>
    <ul class="contact">
      <li class="plain">Your Adress goes here</li>
      <li><svg viewBox="0 0 14 14"><rect x="3" y="1" width="8" height="12" rx="1.5" fill="none" stroke="#fff" stroke-width="1.2"/></svg>0417 828 691</li>
      <li><svg viewBox="0 0 14 14"><path d="M3 1 L5 1 L6 4 L4.5 5 Q6 8.5 9 9.5 L10 8 L13 9 L13 11 Q12 13 10 13 Q3 11 1 4 Q1 2 3 1 Z" fill="none" stroke="#fff" stroke-width="1.1"/></svg>Your other phone#</li>
      <li class="email"><svg viewBox="0 0 14 14"><rect x="1" y="3" width="12" height="8" fill="none" stroke="#fff" stroke-width="1.2"/><path d="M1 3 L7 8 L13 3" fill="none" stroke="#fff" stroke-width="1.2"/></svg>info@trulockinspections.com.au</li>
    </ul>
  </section>

</main>
</body>
</html>
```